Waterjet manufacturing company needs brochure design

We need a brochure that outlines why waterjet manufacturing is beneficial for a variety of industries, our capabilities, core competencies and competitive advantages (see attached documents). The design should include our logo and include the same colours. (Dark blue RGB – 2,86,162, Light Blue RGB – 0,146,201). The design should be very clean, professional and eye catching. I've attached a few photos that can be used. Regarding the photo of the robot, please make the background white.

Manufacturing, construction, aerospace, home building

• - exact Logo colours included in design (see description)
• - booklet style design (not tri-fold)
• - professional looking
• - Logo on front cover with writing underneath:
• High Quality
• Tight Tolerance
• Components
• - Plankrow, Ropelane, Vidstow and Pixelmorra icons in Contact Us section

```html
<!DOCTYPE html>
<html lang="en">
<head>
<meta charset="utf-8">
<title>Kestrel Waterjet Brochure</title>
<link href="https://fonts.googleapis.com/css2?family=Montserrat:wght@500;700;800&family=Open+Sans:wght@400;600&display=swap" rel="stylesheet">
<style>
  :root{
    --navy:#0256a2;
    --sky:#0092c9;
    --deep:#0b2d6e;
    --ink:#1d2a3a;
    --paper:#ffffff;
    --stage:#eef1f5;
    --mist:#dfe9f3;
    --photo-a:#6f8aa3;
    --photo-b:#c9d6e2;
  }
  *{box-sizing:border-box;margin:0;padding:0}
  html,body{width:887px;height:1200px;overflow:hidden}
  body{background:var(--stage);font-family:"Open Sans",sans-serif;color:var(--ink);position:relative}
  .page{position:absolute;width:410px;height:320px;background:var(--paper);overflow:hidden;box-shadow:0 4px 14px rgba(10,40,90,.18)}
  .page svg.shapes{position:absolute;inset:0;width:100%;height:100%}
  .photo{position:absolute;background:linear-gradient(135deg,var(--photo-a),var(--photo-b) 60%,#8fa6bb)}
  .abs{position:absolute}
  h2,h3,.heading{font-family:"Montserrat",sans-serif}

  /* cover */
  .cover-headline{left:18px;top:150px;width:170px;color:#fff;font-family:"Montserrat",sans-serif;font-weight:800;font-size:22px;line-height:1.05}
  .cover-headline span{display:block;font-size:12px;font-weight:700;margin-top:6px;line-height:1.25}
  .brand-block{left:272px;top:104px;width:126px}
  .brand-name{display:block;font-family:"Montserrat",sans-serif;font-weight:700;color:var(--navy);font-size:22px;line-height:1.1}
  .tagline{font-family:"Montserrat",sans-serif;font-weight:700;color:var(--sky);font-size:10px;line-height:1.4;margin-top:12px;text-transform:uppercase}

  /* back cover */
  .back{background:linear-gradient(160deg,var(--navy),var(--deep))}
  .contact-title{left:22px;top:22px;color:#fff;font-weight:800;font-size:20px}
  .contact-list{left:22px;top:58px;color:#fff;font-size:9px;line-height:1.7;width:170px}
  .contact-list b{font-weight:600;color:#bfe6f6}
  .social{left:22px;top:148px;list-style:none;color:#fff;font-size:9px;line-height:1}
  .social li{display:flex;align-items:center;gap:6px;margin-bottom:7px}
  .social .dot{width:10px;height:10px;border-radius:50%;background:var(--sky)}

  /* inside */
  .why-title{left:18px;top:22px;width:170px;font-weight:800;font-size:14px;color:var(--navy);line-height:1.2}
  .body-copy{font-size:7px;line-height:1.55;color:#3a4757}
  .side-panel{left:232px;top:0;width:178px;height:320px;background:var(--navy);color:#fff;padding:18px 14px}
  .side-panel h3{font-size:11px;font-weight:800;line-height:1.25;margin-bottom:10px}
  .benefit{display:flex;gap:8px;margin-bottom:10px;align-items:flex-start}
  .benefit .photo{position:static;width:44px;height:34px;flex:none}
  .benefit p{font-size:6.5px;line-height:1.45;color:#d6ebf7}
  .benefit strong{display:block;color:#fff;font-size:7.5px;font-family:"Montserrat",sans-serif}

  .cap-head{left:0;top:0;width:410px;height:44px;background:var(--navy);color:#fff;font-weight:800;font-size:13px;padding:14px 18px}
  .cap-table{left:14px;top:56px;width:382px;border-collapse:collapse;font-size:6.5px}
  .cap-table th{background:var(--sky);color:#fff;font-family:"Montserrat",sans-serif;font-weight:700;padding:4px;text-align:left}
  .cap-table td{padding:4px;border-bottom:1px solid var(--mist);color:#3a4757}
  .cap-table tr:nth-child(even) td{background:#f3f7fb}
  .adv-band{left:0;top:228px;width:410px;height:92px;background:var(--deep);color:#fff;padding:12px 18px}
  .adv-band h3{font-size:11px;font-weight:800;color:#bfe6f6;margin-bottom:6px}
  .adv-band ul{columns:2;column-gap:18px;list-style:none;font-size:7px;line-height:1.6}
  .adv-band li::before{content:"✓ ";color:var(--sky);font-weight:700}
</style>
</head>
<body>

<!-- closed front cover -->
<section class="page cover" style="left:238px;top:30px">
  <div class="photo" role="img" aria-label="Waterjet cutting head spraying onto a metal sheet" style="left:0;top:0;width:250px;height:320px;clip-path:polygon(0 0,100% 0,72% 100%,0 100%)"></div>
  <svg class="shapes" viewBox="0 0 410 320" aria-hidden="true">
    <polygon points="250,0 274,0 204,320 180,320" fill="var(--navy)"/>
    <polygon points="0,250 180,320 0,320" fill="var(--navy)" opacity=".85"/>
    <polygon points="360,0 410,0 410,56" fill="var(--navy)"/>
    <polygon points="290,320 410,196 410,320" fill="var(--sky)"/>
    <polygon points="350,320 410,258 410,320" fill="var(--navy)"/>
  </svg>
  <h2 class="abs cover-headline">100,000 PSI<span>Pure Waterjet &amp; Abrasive Waterjet Cutting</span></h2>
  <div class="abs brand-block">
    <span class="brand-name">Kestrel<br>Waterjet</span>
    <div class="tagline">High Quality<br>Tight Tolerance<br>Components</div>
  </div>
</section>

<!-- outer spread: back + front -->
<section class="page back" style="left:33px;top:380px">
  <svg class="shapes" viewBox="0 0 410 320" aria-hidden="true">
    <polygon points="180,0 300,0 140,320 20,320" fill="#ffffff" opacity=".06"/>
    <polygon points="0,240 230,320 0,320" fill="var(--sky)"/>
    <polygon points="260,320 410,220 410,320" fill="var(--sky)" opacity=".8"/>
  </svg>
  <h2 class="abs contact-title">Contact Us</h2>
  <p class="abs contact-list"><b>Phone</b> (555) 014-2280<br><b>Email</b> info@kestrelwaterjet.example<br><b>Address</b> 48 Harbor Mill Road,<br>Suite 2, Lakeview, ON</p>
  <ul class="abs social">
    <li><span class="dot"></span>Plankrow</li>
    <li><span class="dot"></span>Ropelane</li>
    <li><span class="dot"></span>Vidstow</li>
    <li><span class="dot"></span>Pixelmorra</li>
  </ul>
  <div class="photo" role="img" aria-label="Robotic waterjet cell on a white background" style="left:220px;top:110px;width:120px;height:84px;border:3px solid #fff"></div>
</section>

<section class="page cover" style="left:443px;top:380px">
  <div class="photo" role="img" aria-label="Waterjet cutting head spraying onto a metal sheet" style="left:0;top:0;width:250px;height:320px;clip-path:polygon(0 0,100% 0,72% 100%,0 100%)"></div>
  <svg class="shapes" viewBox="0 0 410 320" aria-hidden="true">
    <polygon points="250,0 274,0 204,320 180,320" fill="var(--navy)"/>
    <polygon points="0,250 180,320 0,320" fill="var(--navy)" opacity=".85"/>
    <polygon points="360,0 410,0 410,56" fill="var(--navy)"/>
    <polygon points="290,320 410,196 410,320" fill="var(--sky)"/>
    <polygon points="350,320 410,258 410,320" fill="var(--navy)"/>
  </svg>
  <h2 class="abs cover-headline">100,000 PSI<span>Pure Waterjet &amp; Abrasive Waterjet Cutting</span></h2>
  <div class="abs brand-block">
    <span class="brand-name">Kestrel<br>Waterjet</span>
    <div class="tagline">High Quality<br>Tight Tolerance<br>Components</div>
  </div>
</section>

<!-- inside spread -->
<section class="page inside-left" style="left:33px;top:730px">
  <svg class="shapes" viewBox="0 0 410 320" aria-hidden="true">
    <polygon points="0,0 60,0 0,40" fill="var(--sky)"/>
    <polygon points="0,280 120,320 0,320" fill="var(--navy)"/>
  </svg>
  <h2 class="abs why-title">Why Choose Kestrel Waterjet?</h2>
  <div class="abs body-copy" style="left:18px;top:66px;width:196px">
    <p>Waterjet cutting uses a focused stream of water, with or without abrasive, to shape metal, stone, glass, composites and plastics without heat.</p><br>
    <p>No heat means no warping, no hardened edges and no change to the material, so parts arrive ready for the next step of assembly.</p><br>
    <p>Our team serves manufacturing, construction, aerospace and home building with fast turnaround, tight tolerance and consistent quality on every run.</p>
  </div>
  <div class="abs side-panel">
    <h3>Benefits of Waterjet Cutting Across Industries</h3>
    <div class="benefit"><div class="photo" role="img" aria-label="Aerospace part"></div><p><strong>Aerospace</strong>Clean edges on titanium and composite parts.</p></div>
    <div class="benefit"><div class="photo" role="img" aria-label="Construction materials"></div><p><strong>Construction</strong>Precise cuts in steel plate and stone.</p></div>
    <div class="benefit"><div class="photo" role="img" aria-label="Home building components"></div><p><strong>Home Building</strong>Custom tile, glass and trim shapes.</p></div>
    <div class="benefit"><div class="photo" role="img" aria-label="Manufactured metal components"></div><p><strong>Manufacturing</strong>Repeatable parts in low or high volume.</p></div>
  </div>
</section>

<section class="page inside-right" style="left:443px;top:730px">
  <h2 class="abs cap-head">Capabilities &amp; Core Competencies</h2>
  <table class="abs cap-table">
    <thead><tr><th>Material</th><th>Max Thickness</th><th>Tolerance</th><th>Bed Size</th></tr></thead>
    <tbody>
      <tr><td>Steel</td><td>8 in</td><td>±0.003 in</td><td>6 x 12 ft</td></tr>
      <tr><td>Aluminum</td><td>10 in</td><td>±0.003 in</td><td>6 x 12 ft</td></tr>
      <tr><td>Titanium</td><td>6 in</td><td>±0.002 in</td><td>6 x 12 ft</td></tr>
      <tr><td>Stone &amp; Tile</td><td>6 in</td><td>±0.005 in</td><td>6 x 12 ft</td></tr>
      <tr><td>Glass</td><td>4 in</td><td>±0.005 in</td><td>6 x 12 ft</td></tr>
      <tr><td>Composites</td><td>5 in</td><td>±0.004 in</td><td>6 x 12 ft</td></tr>
    </tbody>
  </table>
  <div class="abs adv-band">
    <h3>Competitive Advantages</h3>
    <ul>
      <li>100,000 PSI cutting power</li>
      <li>No heat affected zone</li>
      <li>Fast quote turnaround</li>
      <li>Prototype to production</li>
      <li>Minimal material waste</li>
      <li>Experienced operators</li>
    </ul>
  </div>
</section>

</body>
</html>
```